4D Hush Little Nest Luxury Ultrasound Billboard

Design a HIGH-END, MODERN billboard for my private prenatal ultrasound studio, 4D Hush Little Nest, located in Pace, Florida.
This billboard will be viewed by drivers traveling at highway speeds, so it must be extremely clean, simple, and readable within 6 seconds.
About My Business
4D Hush Little Nest is a private prenatal ultrasound studio specializing in:
Highest technology 4D/HD Ultrasounds
Early Gender Determination
Pregnancy Confirmation
I have been serving families for nearly 10 years and is known for creating a memorable experience, not just an ultrasound appointment.
Design Style
I DO NOT want:
Flowers
Leaves
Swirls
Glitter
Hearts everywhere
Busy backgrounds
Generic maternity stock graphics
I DO want:
Modern
Luxury
Upscale
Clean
Professional
Eye-catching
Premium medical spa feel
Colors
Use colors from my logo:
LOGO Green ( or a deep green)
Black
White
Soft Gold accents
Images:
Incorporate my professional headshot in a clean, modern way, logo, and the ultrasound images
Text
Keep wording minimal.
Primary Headline ( OPEN TO IDEAS) :
EXAMPLES ( WOULD RATHER SOMETHING MORE CATCHY)
" ADVANCED IMAGING. UNFORGETTABLE MOMENTS"
"MEET YOUR BABY BEFORE BIRTH"
Under headline:
4D Ultrasound • Early Gender • Pregnancy Confirmation
Business Name:
4D Hush Little Nest
Private Prenatal Ultrasound Studio
Phone Number:
850-471-3905
Important
This billboard must be readable in 5–6 seconds from a moving vehicle.
Less text is better.
The phone number and business name must be visible from a distance.
The design should feel like a premium brand that immediately tells expecting parents:
“This is where I go to see my baby.”
Files Provided
Official logo
Headshot
Ultrasound images
Don’t make this look like a medical office billboard.
Make it look like a luxury baby experience billboard. That’s what separates 4D Hush Little Nest from hospitals, OB offices, and all the new studios popping up around you. The emotional connection is what gets moms to book. ❤️
Billboard Size - 10.6” x 36”

```html
<!DOCTYPE html>
<html lang="en">
<head>
<meta charset="utf-8">
<title>4D Hush Little Nest Billboard</title>
<link rel="stylesheet" href="https://fonts.googleapis.com/css2?family=Libre+Caslon+Text:wght@700&family=Montserrat:wght@600;700&display=swap">
<style>
  :root {
    --frame-green: #4a5a52;
    --deep-black: #050505;
    --soft-gold: #bb9638;
    --gold-text: #c79d3a;
    --white: #ffffff;
    --logo-grey: #6a7470;
    --ultra-dark: #2a0f0b;
    --ultra-mid: #8e4a3c;
    --ultra-light: #c98a78;
    --studio-light: #eceae6;
    --studio-mid: #d9d6d0;
    --scrub-green: #3f5a3e;
  }
  * { margin: 0; padding: 0; box-sizing: border-box; }
  html, body { width: 1200px; height: 375px; overflow: hidden; background: #ffffff; }
  .billboard {
    position: relative;
    width: 1200px;
    height: 375px;
    background: var(--frame-green);
    border-radius: 6px;
    overflow: hidden;
  }
  .ultrasound-photo {
    position: absolute;
    left: 6px; top: 5px;
    width: 340px; height: 363px;
    border-radius: 42px 0 0 42px;
    background: radial-gradient(ellipse at 30% 45%, var(--ultra-light) 0%, var(--ultra-mid) 40%, var(--ultra-dark) 100%);
  }
  .headshot-photo {
    position: absolute;
    right: 6px; top: 5px;
    width: 330px; height: 363px;
    border-radius: 0 42px 42px 0;
    background: linear-gradient(90deg, var(--studio-mid) 0%, var(--studio-light) 35%, var(--scrub-green) 70%, var(--studio-light) 100%);
  }
  .message-panel {
    position: absolute;
    left: 305px; top: 5px;
    width: 620px; height: 363px;
    border: 6px solid var(--soft-gold);
    border-radius: 46px;
    background: var(--deep-black);
    text-align: center;
    color: var(--white);
  }
  .brand-mark {
    position: absolute;
    left: 231px; top: 37px;
    width: 146px; height: 70px;
    border: 1.5px solid var(--logo-grey);
    border-radius: 8px;
    display: flex; flex-direction: column; align-items: center; justify-content: center;
    gap: 6px;
  }
  .brand-name {
    font-family: "Montserrat", sans-serif;
    font-weight: 700;
    font-size: 13px;
    color: var(--gold-text);
  }
  .brand-rule { width: 124px; height: 1px; background: var(--soft-gold); }
  .brand-tagline {
    font-family: "Montserrat", sans-serif;
    font-weight: 600;
    font-size: 6px;
    letter-spacing: 0.3px;
    color: var(--logo-grey);
  }
  .headline {
    position: absolute;
    left: 0; right: 0; top: 128px;
    font-family: "Libre Caslon Text", serif;
    font-weight: 700;
    font-size: 46px;
    line-height: 50px;
    letter-spacing: 0.5px;
  }
  .divider {
    position: absolute;
    left: 229px; top: 240px;
    width: 150px; height: 1px;
    background: var(--soft-gold);
  }
  .services {
    position: absolute;
    left: 0; right: 0; top: 262px;
    font-family: "Montserrat", sans-serif;
    font-weight: 700;
    font-size: 16.5px;
    letter-spacing: 0.4px;
    color: var(--gold-text);
  }
  .phone {
    position: absolute;
    left: 0; right: 0; top: 294px;
    display: flex; align-items: center; justify-content: center; gap: 10px;
    font-family: "Montserrat", sans-serif;
    font-weight: 700;
    font-size: 38px;
    letter-spacing: 0.5px;
  }
  .phone-icon { width: 38px; height: 38px; }
</style>
</head>
<body>
  <div class="billboard">
    <div class="ultrasound-photo" role="img" aria-label="4D ultrasound image of twin babies face to face"></div>
    <div class="headshot-photo" role="img" aria-label="Professional headshot of the studio owner holding an ultrasound probe"></div>

    <div class="message-panel">
      <div class="brand-mark">
        <span class="brand-name">4D Hush Little Nest</span>
        <span class="brand-rule"></span>
        <span class="brand-tagline">PRENATAL ULTRASOUND STUDIO</span>
      </div>

      <h1 class="headline">MEET YOUR BABY<br>BEFORE BIRTH</h1>

      <div class="divider"></div>

      <p class="services">4D ULTRASOUND • EARLY GENDER • PREGNANCY CONFIRMATION</p>

      <p class="phone">
        <svg class="phone-icon" viewBox="0 0 40 40" aria-hidden="true">
          <circle cx="20" cy="20" r="18" fill="var(--soft-gold)" stroke="var(--white)" stroke-width="3"/>
          <path d="M14 11c1-1 2.5-.8 3 .4l1.6 3.4c.4.9.1 1.9-.6 2.4l-1.3 1c.9 2 2.3 3.6 4.2 4.6l1.1-1.2c.7-.7 1.7-.9 2.5-.4l3.2 1.9c1.1.6 1.2 2.1.3 3l-1.6 1.6c-1 1-2.6 1.3-4 .7-5.2-2.2-9-6.4-10.6-11.6-.4-1.4 0-2.9 1-3.9z" fill="var(--white)"/>
        </svg>
        <span>850-471-3905</span>
      </p>
    </div>
  </div>
</body>
</html>
```